One-Page Designed - Top 5 Tips for Curly Hair

I need a one-pager designed that looks friendly, informative, and natural, but that can be used as a PDF download for a website. the current website is not launched yet but the link is www.fernstudiodover.net for reference.

This piece will be the piece we send to clients once they log into our website and subscribe so it is a very important piece.

Fern Salon is an eco-friendly and holistically minded salon. Through research and education, we’ve curated a selection of less toxic hair color and hair styling products that offer professional results with the most natural ingredients on the market today. Whether you’re looking for a great haircut, expert grey coverage, bouncy curls or an amazing balayage, we’re here for you.

We’re dedicated to improving the locks of curly girls in the greater Boston area. We are curly hair experts who are committed to continuing education on the lasted curly hair cutting and coloring techniques. We’ll keep your curls healthy and fabulous with our carefully curated collection of products too.

Target Market(s)

Curly Hair Girls Who Want to Go to Natural Product Salon

Industry/Entity Type

Hair And Beauty

Font styles to use
Other font styles liked:
• Dancing Script and Arial Nova

Requirements
Must have
• Should have graphics that call out the tips and then have the blocks that go with them as the descriptions. Should be fun, friendly and informative. Final product should be send as a PDF.
• Colors should go with Hex: #5BC2E7 and Hex: #686A66 and Hex: #C8C9C7
• It should include their logo and a photo of the owner Marisol.
Nice to have
• Images that reflect the copy.

```html
<!DOCTYPE html>
<html lang="en">
<head>
<meta charset="utf-8">
<title>Top 5 Tips for Curly Hair – Fern Salon</title>
<link rel="stylesheet" href="https://fonts.googleapis.com/css2?family=Arimo:wght@400;700&family=Dancing+Script:wght@400;500&family=Roboto+Condensed:wght@300;400&display=swap">
<style>
  :root {
    --sky: #4dc3ee;
    --brand-blue: #5BC2E7;
    --ink: #686A66;
    --mist: #C8C9C7;
    --footer: #b1b2b0;
    --stage: #3a3a3c;
    --white: #ffffff;
  }
  * { box-sizing: border-box; margin: 0; padding: 0; }
  html, body { width: 1200px; height: 1200px; overflow: hidden; background: var(--stage); }
  .flyer {
    position: absolute; left: 200px; top: 34px;
    width: 800px; height: 1132px; overflow: hidden;
    background: var(--sky);
    font-family: "Arimo", Arial, sans-serif;
  }
  .hero {
    position: absolute; left: 0; top: 0; width: 800px; height: 600px;
    background:
      radial-gradient(ellipse 230px 300px at 600px 320px, rgba(214,70,60,.35), rgba(214,70,60,0) 70%),
      linear-gradient(180deg, #fbfcfd 0%, #f1f5f8 55%, #e6eef3 80%, var(--sky) 100%);
  }
  .logo {
    position: absolute; left: 508px; top: 46px; width: 240px;
    font-weight: 700; font-size: 36px; letter-spacing: 1px; white-space: nowrap;
    color: var(--brand-blue);
  }
  .kicker { position: absolute; left: 20px; top: 150px; width: 320px; height: 200px; }
  .title {
    position: absolute; left: 110px; top: 252px;
    font-weight: 700; font-size: 56px; line-height: 46px; letter-spacing: -2.5px;
    color: var(--brand-blue);
  }
  .intro {
    position: absolute; left: 114px; top: 363px;
    font-size: 18.4px; line-height: 22.6px; color: var(--ink); white-space: nowrap;
  }
  .tips { position: absolute; left: 0; top: 0; }
  .tip { position: absolute; left: 0; width: 800px; }
  .tip-label {
    position: absolute; right: 457px; text-align: right; white-space: nowrap;
    font-family: "Dancing Script", cursive; font-weight: 400; font-size: 15px; line-height: 19.5px;
    color: var(--white); z-index: 2;
  }
  .tip-number {
    position: absolute; left: 292px; top: -8px; width: 50px; text-align: center;
    font-weight: 700; font-size: 58px; color: rgba(255,255,255,.28);
  }
  .tip-body {
    position: absolute; left: 355px; width: 392px;
    font-family: "Roboto Condensed", sans-serif; font-size: 11.3px; line-height: 16px;
    color: var(--white);
  }
  .owner-card { position: absolute; left: 26px; top: 870px; width: 196px; height: 262px; z-index: 3; }
  .owner-card svg { position: absolute; left: 0; top: 0; }
  .owner-photo {
    position: absolute; left: 38px; top: -58px; width: 122px; height: 122px; border-radius: 50%;
    border: 3px solid var(--brand-blue);
    background: radial-gradient(circle at 50% 45%, #c99a82 0%, #6d4a3a 55%, #2e2320 100%);
  }
  .owner-name {
    position: absolute; left: 0; top: 73px; width: 196px; text-align: center;
    font-family: "Dancing Script", cursive; font-size: 19px; color: var(--brand-blue);
  }
  .owner-rule { position: absolute; left: 30px; top: 100px; width: 146px; height: 1px; background: var(--brand-blue); }
  .owner-bio {
    position: absolute; left: 6px; top: 108px; width: 184px; text-align: center;
    font-family: "Roboto Condensed", sans-serif; font-weight: 300; font-size: 14px; line-height: 18px;
    color: var(--ink);
  }
  .footer {
    position: absolute; left: 0; top: 1092px; width: 800px; height: 40px; background: var(--footer);
  }
  .footer-contact {
    position: absolute; left: 283px; top: 15px;
    font-weight: 700; font-size: 8.6px; letter-spacing: 3.1px; color: var(--white);
  }
</style>
</head>
<body>
<main class="flyer">
  <div class="hero" role="img" aria-label="Photo of a smiling woman with long curly hair in sunglasses and a red top taking a selfie against a bright sky"></div>

  <div class="logo">FERN SALON</div>

  <svg class="kicker" viewBox="0 0 320 200" aria-label="A Curly Stylists'">
    <defs><path id="kicker-arc" d="M30 190 Q 90 40 290 95"/></defs>
    <text font-family="Dancing Script, cursive" font-size="46" fill="#5BC2E7">
      <textPath href="#kicker-arc">A Curly Stylists'</textPath>
    </text>
  </svg>

  <h1 class="title">Top 5 Tips for<br>Curly Hair</h1>

  <p class="intro">I get it. Everyone is looking for ease and<br>order in their busy lives.&nbsp; Whether you’ve<br>just ditched your flat iron or you’re a<br>long-time curly girl looking for fresh<br>direction, here are our top tips for luscious<br>curls and waves.</p>

  <section class="tips">
    <article class="tip" style="top:610px">
      <span class="tip-number">1</span>
      <h2 class="tip-label">Embrace the diversity<br>of your curls</h2>
      <p class="tip-body">Yes, you will have “curl diversity” everyday and that’s okay. Being consistent with your haircare routine and avoiding the temptation to blow dry or straighten will do wonders for your hair over the long term. I promise, your overall curl or wave pattern will improve over time. I also promise that you will never have the same head of curls twice. Variety is the spice of life!</p>
    </article>
    <article class="tip" style="top:704px">
      <span class="tip-number">2</span>
      <h2 class="tip-label">Keep your cleanser<br>gentle and leave in a<br>little bit of your<br>conditioner</h2>
      <p class="tip-body">Yes, you will have “curl diversity” everyday and that’s okay. Being consistent with your haircare routine and avoiding the temptation to blow dry or straighten will do wonders for your hair over the long term. I promise, your overall curl or wave pattern will improve over time. I also promise that you will never have the same head of curls twice. Variety is the spice of life!</p>
    </article>
    <article class="tip" style="top:803px">
      <span class="tip-number">3</span>
      <h2 class="tip-label">Avoid silicones and<br>sulfates</h2>
      <p class="tip-body">You’ve heard this (pretty much everywhere) before but that’s only because it’s true. Silicones coat the hair and are extremely difficult to remove, leaving the hair with an altered texture and rendering it impervious to deep conditioning.&nbsp; Use only reputable hair care products like those from Meadowleaf Organics or Coil Haven. Beware of hidden silicones. They can be in the “fragrance” portion of the ingredient list. (thanks to Dana Whitlow for that new knowledge.</p>
    </article>
    <article class="tip" style="top:914px">
      <span class="tip-number">4</span>
      <h2 class="tip-label">Rest easy</h2>
      <p class="tip-body">Wrap your curls or waves in a silk scarf to avoid friction. If you’re rough sleeper and you wake up with your scarf wrapped somewhere between your neck and your armpit (me), a silk pillow case is a better and safer option. Less friction= smoother curls.</p>
    </article>
    <article class="tip" style="top:979px">
      <span class="tip-number">5</span>
      <h2 class="tip-label">Cutting curls every<br>6-10 weeks</h2>
      <p class="tip-body">I’m not saying this because I’m a stylist, I swear. I’m saying this because I care about curly hair. Cutting curls every 6-10 weeks, depending on the length and curl type is essential to great hair health. Keeping your ends blunt and free of splits and frays will make styling easier and is especially important of you’re growing your hair longer. We all know how long that takes when you’re a curly girl.</p>
    </article>
  </section>

  <footer class="footer">
    <p class="footer-contact">WWW.FERNSTUDIODOVER.NET ~FERNSTUDIODOVER@MAIL.COM</p>
  </footer>

  <aside class="owner-card">
    <svg width="196" height="262" viewBox="0 0 196 262">
      <polygon points="0,0 196,34 196,245 0,245" fill="#ffffff"/>
      <rect x="0" y="245" width="196" height="17" fill="#4dc3ee"/>
    </svg>
    <div class="owner-photo" role="img" aria-label="Portrait photo of salon owner Marisol Vantrelli"></div>
    <p class="owner-name">Marisol Vantrelli</p>
    <div class="owner-rule"></div>
    <p class="owner-bio">Marisol is the owner of Fern Salon in Dover and Halden, MA. She is a Spiralis advanced curly hair stylist and is certified in the Ring by Ring method. She is a curl advocate and a lover of natural and organic products.</p>
  </aside>
</main>
</body>
</html>
```